Crestline Gas and Plumbing Business Card Design

I am after a business card design for my plumbing business called 'Crestline Gas & Plumbing'. I do all types of plumbing and gas work and specialise in general maintenance plumbing. Would like to see designs using current logo

Industry/Entity Type

Plumbing

Contact Information for Business Card

Name - Dale Whitcombe
Phone number - 0455163027
Email - admin@crestlinegasandplumbing.example.com.au
ABN - 68204915336

```html
<!DOCTYPE html>
<html lang="en">
<head>
<meta charset="utf-8">
<title>Crestline Gas &amp; Plumbing – Business Card</title>
<link rel="stylesheet" href="https://fonts.googleapis.com/css2?family=Oswald:wght@500&family=Tinos&display=swap">
<style>
  :root {
    --backdrop: #95bcc0;
    --card: #232323;
    --card-edge: #1b1b1b;
    --orange: #f39a1e;
    --orange-deep: #e4571a;
    --white: #f4f4f4;
    --brand-blue: #2f7fd6;
    --ink-dark: #1e1e1e;
  }
  * { margin: 0; padding: 0; box-sizing: border-box; }
  html, body { width: 1200px; height: 960px; overflow: hidden; }
  body {
    background: var(--backdrop);
    display: flex;
    flex-direction: column;
    align-items: center;
    justify-content: center;
    gap: 50px;
  }
  .card {
    position: relative;
    width: 700px;
    height: 400px;
    background: var(--card);
    overflow: hidden;
    box-shadow: 0 10px 24px rgba(0,0,0,0.25);
  }
  .brand {
    position: absolute;
    display: flex;
    align-items: center;
    gap: 14px;
    font-family: "Oswald", sans-serif;
    font-weight: 500;
    color: var(--brand-blue);
    text-transform: uppercase;
    letter-spacing: 1px;
    line-height: 1;
    white-space: nowrap;
  }
  .brand-dot {
    width: 26px; height: 26px;
    border-radius: 50%;
    background: var(--orange);
    flex: none;
  }

  /* Front face */
  .card-front .accent-line {
    position: absolute;
    left: 0; top: 196px;
    width: 170px; height: 4px;
    background: linear-gradient(90deg, var(--orange-deep), var(--orange));
  }
  .card-front .brand { left: 186px; top: 180px; font-size: 34px; }
  .card-front .corner-band {
    position: absolute;
    left: 0; bottom: 0;
    width: 100%; height: 70px;
  }

  /* Back face */
  .card-back .holder {
    position: absolute;
    right: 40px; top: 40px;
    font-family: "Oswald", sans-serif;
    font-weight: 500;
    font-size: 34px;
    color: var(--white);
    text-transform: uppercase;
    padding-bottom: 6px;
    border-bottom: 3px solid var(--white);
  }
  .card-back .brand {
    left: 50%; top: 190px;
    transform: translateX(-50%);
    font-size: 32px;
  }
  .card-back .contact-band {
    position: absolute;
    left: 0; right: 0; bottom: 0;
    height: 86px;
    background: linear-gradient(180deg, var(--orange) 0%, var(--orange-deep) 100%);
    display: flex;
    align-items: center;
    justify-content: center;
    gap: 40px;
    font-family: "Tinos", serif;
    font-size: 19px;
    color: var(--ink-dark);
    letter-spacing: 1px;
  }
  .contact-band::before {
    content: "";
    position: absolute;
    left: 0; right: 0; top: 0;
    height: 8px;
    background: var(--card);
    opacity: 0.0;
  }
  .contact-item { display: flex; align-items: center; gap: 10px; }
  .contact-item svg { width: 20px; height: 20px; flex: none; }
  .at-sign { font-family: "Oswald", sans-serif; font-size: 22px; font-weight: 500; }
</style>
</head>
<body>

  <section class="card card-front" aria-label="Business card front">
    <div class="accent-line"></div>
    <div class="brand"><span class="brand-dot"></span>Crestline Gas &amp; Plumbing</div>
    <svg class="corner-band" viewBox="0 0 700 70" preserveAspectRatio="none" aria-hidden="true">
      <defs>
        <linearGradient id="bandGrad" x1="0" y1="0" x2="0" y2="1">
          <stop offset="0" stop-color="#f6b02a"/>
          <stop offset="1" stop-color="#e4571a"/>
        </linearGradient>
      </defs>
      <polygon points="0,10 210,50 210,70 0,70" fill="url(#bandGrad)"/>
    </svg>
  </section>

  <section class="card card-back" aria-label="Business card back">
    <div class="holder">Dale Whitcombe</div>
    <div class="brand"><span class="brand-dot"></span>Crestline Gas &amp; Plumbing</div>
    <div class="contact-band">
      <span class="contact-item">
        <svg viewBox="0 0 24 24" aria-hidden="true"><path fill="#1e1e1e" d="M6.6 10.8a15.2 15.2 0 0 0 6.6 6.6l2.2-2.2a1 1 0 0 1 1-.25 11.4 11.4 0 0 0 3.6.57 1 1 0 0 1 1 1V20a1 1 0 0 1-1 1A17 17 0 0 1 3 4a1 1 0 0 1 1-1h3.5a1 1 0 0 1 1 1c0 1.25.2 2.45.57 3.57a1 1 0 0 1-.25 1z"/></svg>
        0455163027
      </span>
      <span class="contact-item">
        <span class="at-sign">@</span>
        admin@crestlinegasandplumbing.example.com.au
      </span>
    </div>
  </section>

</body>
</html>
```